Happy Birthday Cards (from Law Firm)

Need classy, professional AND polished Happy Birthday Cards from law firm.

Please tie in the firm logo and colors somewhere with the picture on front or inside(but not used too many times)

Include company logo somewhere on the card, firm name (Verona Pask Law, PLLC) www.veronapasklaw.com
Updates

Reason: Thank you for your patience. Had a family emergency.

Target Market(s)

Law firm clients ages 30 - 99

Industry/Entity Type

Law Firm

Font styles to use
Serif
Sans Serif
Decorative
Script

Requirements
Must have
• Must be classy, elegant, professional, polished from a business
• Birthday wish or message - you suggest one.
• For example "Enjoy every moment of your life. May everyday bring something new and exciting for you. May your birthday be as amazing as you."
Nice to have
• Would like several birthday card templates (for male/for female); traditional/fun

```html
<!DOCTYPE html>
<html lang="en">
<head>
<meta charset="utf-8">
<title>Birthday Card – Verona Pask Law, PLLC</title>
<link href="https://fonts.googleapis.com/css2?family=Oswald:wght@500&family=Kaushan+Script&family=Merriweather:wght@400&display=swap" rel="stylesheet">
<style>
  :root {
    --bg: #ede8f0;
    --paper: #ffffff;
    --navy: #174f6e;
    --sky: #2a86b4;
    --lime: #c3c62a;
    --orange: #f05a28;
    --flame: #f2a533;
    --flame-core: #fbe08a;
    --rule: #3a3a3a;
  }
  * { margin: 0; padding: 0; box-sizing: border-box; }
  html, body {
    width: 1200px; height: 1029px; overflow: hidden;
    background: var(--bg);
  }
  .card {
    position: absolute; left: 266px; top: 41px;
    width: 668px; height: 946px;
    background: var(--paper);
    box-shadow: 0 2px 10px rgba(60, 40, 80, 0.12);
  }
  .card-frame { position: absolute; inset: 0; }
  .firm-mark {
    position: absolute; left: 285px; top: 67px;
    width: 96px; height: 96px; border-radius: 50%;
    background: var(--navy);
  }
  .firm-rule {
    position: absolute; left: 192px; width: 284px; height: 0;
    border-top: 1.5px solid var(--rule);
  }
  .firm-rule.top { top: 169px; }
  .firm-rule.bottom { top: 246px; }
  .firm-name {
    position: absolute; left: 0; width: 100%; top: 190px;
    text-align: center;
    font-family: "Merriweather", serif; font-weight: 400;
    font-size: 22px; line-height: 34px; color: var(--navy);
  }
  .candle { position: absolute; left: 313px; top: 346px; }
  .wish {
    position: absolute; left: 0; width: 100%;
    text-align: center;
    font-family: "Oswald", sans-serif; font-weight: 500;
    text-transform: uppercase; letter-spacing: 0.2px;
  }
  .wish span { position: absolute; left: 0; width: 100%; display: block; }
  .wish .lime { color: var(--lime); }
  .wish .orange { color: var(--orange); }
  .wish .sky { color: var(--sky); }
  .greeting {
    position: absolute; left: 0; width: 100%;
    text-align: center;
    font-family: "Kaushan Script", cursive; font-weight: 400;
    color: var(--navy); font-size: 70px; line-height: 86px;
  }
  .website {
    position: absolute; left: 0; width: 100%; top: 861px;
    text-align: center;
    font-family: "Merriweather", serif;
    font-size: 21px; line-height: 28px; color: var(--navy);
  }
</style>
</head>
<body>
  <main class="card">
    <svg class="card-frame" width="668" height="946" viewBox="0 0 668 946" aria-hidden="true">
      <path fill="var(--navy)" d="M45,15 H623 A28,28 0 0 0 651,43 V904 A28,28 0 0 0 623,932 H45 A28,28 0 0 0 17,904 V43 A28,28 0 0 0 45,15 Z"/>
      <path fill="var(--sky)" d="M51,27 H617 A26,26 0 0 0 639,49 V898 A26,26 0 0 0 617,920 H51 A26,26 0 0 0 29,898 V49 A26,26 0 0 0 51,27 Z"/>
      <path fill="var(--paper)" d="M57,36 H611 A24,24 0 0 0 630,55 V892 A24,24 0 0 0 611,911 H57 A24,24 0 0 0 38,892 V55 A24,24 0 0 0 57,36 Z"/>
    </svg>

    <div class="firm-mark" aria-hidden="true"></div>
    <div class="firm-rule top"></div>
    <div class="firm-name">Verona Pask Law, PLLC</div>
    <div class="firm-rule bottom"></div>

    <svg class="candle" width="40" height="100" viewBox="0 0 40 100" aria-hidden="true">
      <path fill="var(--flame)" d="M20,2 C27,12 29,20 29,25 A9,9 0 0 1 11,25 C11,20 13,12 20,2 Z"/>
      <path fill="var(--flame-core)" d="M20,13 C24,19 25,23 25,26 A5,5 0 0 1 15,26 C15,23 16,19 20,13 Z"/>
      <rect x="10" y="40" width="21" height="57" rx="2" fill="var(--navy)"/>
    </svg>

    <p class="wish">
      <span class="lime" style="top:444px;font-size:14px;line-height:20px;">Enjoy every moment</span>
      <span class="lime" style="top:461px;font-size:20px;line-height:26px;">of your life!</span>
      <span class="orange" style="top:486px;font-size:17px;line-height:24px;">May everyday bring</span>
      <span class="orange" style="top:507px;font-size:17px;line-height:24px;">something new and</span>
      <span class="orange" style="top:527px;font-size:21px;line-height:28px;">exciting for you.</span>
      <span class="sky" style="top:552px;font-size:20px;line-height:26px;">May your birthday be</span>
      <span class="sky" style="top:574px;font-size:20px;line-height:26px;">as amazing as you are!</span>
    </p>

    <h1 class="greeting" style="top:618px;">Happy Birthday!</h1>
    <p class="greeting" style="top:708px;">To You!</p>

    <p class="website">www.veronapasklaw.com</p>
  </main>
</body>
</html>
```